Stationary for Keeping Steady

we are in the process of creating a more professional image for our company Keeping Steady Paramedical Services. We have recently had a new logo and general brochure designed using artpitchhub and have been impressed by the quality of submissions.

We need:
- Letterhead (A4)
- Business Cards
- With compliments slips
- Email stationary

Letterhead information:
Address - 47 Wattlebrook Drive, Fernhollow Vic 3091
Phone - 1800 462 817
email - enquiries@keepsteady.com.au
Internet - www.keepsteady.com.au
ABN - 82 463 915 207
ACN - 264 871 035

Files need to be able to be edited in Illustrator CS2

Business Cards / with compliments slips / email stationary:
Double sided.
One side to have Name, Mobile number, company phone 1800462817, email, internet address

Files need to be able to be edited in Illustrator CS2 (except email stationary)

Our website is www.keepsteady.com.au for more information. Do not base designs on the website as it will eventually be revised.

Target Market(s)

Australian based businesses, government departments and schools. We specialise in corporate customers rather than public first aid course

Industry/Entity Type

Internet

Requirements
Must have
• Where applicable file to be editable in illustrator CS2 to allow future alterations.

```html
<!DOCTYPE html>
<html lang="en">
<head>
<meta charset="utf-8">
<title>Keeping Steady Paramedical Services – Letterhead</title>
<link href="https://fonts.googleapis.com/css2?family=Mulish:wght@400;800&display=swap" rel="stylesheet">
<style>
  :root {
    --brand-red: #e3232a;
    --band-black: #0c0c0c;
    --band-grey: #3a3a3a;
    --paper: #ffffff;
    --footer-text: #e6e6e6;
  }
  html, body {
    margin: 0;
    padding: 0;
    overflow: hidden;
    background: var(--paper);
  }
  .letterhead {
    position: relative;
    width: 849px;
    height: 1200px;
    background: var(--paper);
    overflow: hidden;
    font-family: "Mulish", sans-serif;
  }
  .brand {
    position: absolute;
    left: 34px;
    top: 34px;
    display: flex;
    align-items: flex-start;
    gap: 16px;
    color: var(--brand-red);
    font-weight: 800;
  }
  .brand-mark {
    width: 96px;
    height: 96px;
    background: var(--brand-red);
    flex: none;
  }
  .brand-name {
    margin: 4px 0 0;
    font-size: 46px;
    line-height: 1;
    letter-spacing: -0.5px;
  }
  .brand-sub {
    display: block;
    margin-top: 8px;
    font-size: 22px;
    letter-spacing: 0;
  }
  .footer-band {
    position: absolute;
    left: 0;
    bottom: 0;
    width: 849px;
    height: 220px;
  }
  .contact {
    position: absolute;
    right: 28px;
    bottom: 58px;
    margin: 0;
    text-align: right;
    color: var(--footer-text);
    font-size: 11px;
    line-height: 19px;
    font-style: normal;
  }
</style>
</head>
<body>
<main class="letterhead">
  <header class="brand">
    <span class="brand-mark" aria-hidden="true"></span>
    <h1 class="brand-name">Keeping Steady<span class="brand-sub">Paramedical Services Pty Ltd</span></h1>
  </header>

  <svg class="footer-band" viewBox="0 980 849 220" aria-hidden="true">
    <defs>
      <linearGradient id="bandShade" x1="0" y1="0" x2="1" y2="0">
        <stop offset="0" stop-color="var(--band-grey)"/>
        <stop offset="0.45" stop-color="var(--band-black)"/>
        <stop offset="1" stop-color="var(--band-black)"/>
      </linearGradient>
    </defs>
    <path d="M0 1190 C170 1066 490 996 849 980 L849 1200 L0 1200 Z" fill="var(--brand-red)"/>
    <path d="M0 1200 C180 1080 500 1010 849 995 L849 1200 Z" fill="url(#bandShade)"/>
  </svg>

  <address class="contact">
    47 Wattlebrook Drive, Fernhollow Vic 3091<br>
    P: 1800 462 817 E: enquiries@keepsteady.com.au &nbsp;W: www.keepsteady.com.au<br>
    ABN : 82 463 915 207 ACN : 264 871 035
  </address>
</main>
</body>
</html>
```